Business Card Design

New business card design

Target Market(s)

Residential & Commercial Property Managers

Industry/Entity Type

Plumbing Services

Contact Information for Business Card

Name - Owen Tredgold, title - Director, Phone Number - 0431 862 507, email - owen@rvb-plumbing.com.au, Company ABN - 73 215 904 386,

Font styles to use
Sans Serif

Colors
0054AA
0677BA
7BADD7
CADEEF
E8F1F8

```html
<!DOCTYPE html>
<html lang="en">
<head>
<meta charset="utf-8">
<title>RVB Plumbing Services – Business Card</title>
<link rel="stylesheet" href="https://fonts.googleapis.com/css2?family=Open+Sans:wght@400;700&family=Roboto+Condensed:wght@300;400&display=swap">
<style>
  :root {
    --ink: #0a0f12;
    --sky: #00ccff;
    --aqua: #00ffff;
    --accent: #4dd4ff;
    --silver: #c8c8c8;
    --edge: #9a9a9a;
    --paper: #ffffff;
  }
  html, body {
    margin: 0;
    padding: 0;
    width: 898px;
    height: 1200px;
    overflow: hidden;
    background: var(--paper);
  }
  .sheet {
    position: relative;
    width: 898px;
    height: 1200px;
  }
  .card {
    position: absolute;
    left: 0;
    width: 898px;
    height: 539px;
    display: block;
  }
  .card--front { top: 0; }
  .card--back { top: 623px; }
  .card-edge { fill: var(--paper); stroke: var(--edge); stroke-width: 1; }
  .band-silver { fill: var(--silver); }
  .band-sky { fill: var(--sky); }
  .band-aqua { fill: var(--aqua); }
  .company-name {
    font-family: "Roboto Condensed", sans-serif;
    font-weight: 400;
    fill: var(--ink);
  }
  .person-name {
    font-family: "Open Sans", sans-serif;
    font-weight: 700;
    fill: var(--ink);
  }
  .person-title {
    font-family: "Open Sans", sans-serif;
    font-weight: 400;
    fill: var(--ink);
  }
  .contact-line {
    font-family: "Roboto Condensed", sans-serif;
    font-weight: 400;
    fill: var(--ink);
  }
  .abn-line {
    font-family: "Roboto Condensed", sans-serif;
    font-weight: 300;
    fill: var(--paper);
  }
  .icon-fill { fill: var(--accent); }
  .icon-stroke { fill: none; stroke: var(--paper); stroke-width: 1.6; }
  .side-label {
    position: absolute;
    font-family: Arial, Helvetica, sans-serif;
    font-size: 26px;
    color: #000;
    margin: 0;
    line-height: 1;
  }
  .side-label--front { left: 7px; top: 561px; }
  .side-label--back { right: 6px; top: 1176px; }
</style>
</head>
<body>
<div class="sheet">

  <svg class="card card--front" viewBox="0 0 898 539" xmlns="http://www.w3.org/2000/svg">
    <rect class="card-edge" x="0.5" y="0.5" width="897" height="538"/>
    <polygon class="band-silver" points="645,539 898,305 898,539"/>
    <polygon class="band-sky" points="663,539 898,320 898,539"/>
    <polygon class="band-aqua" points="767,539 898,416 898,539"/>
    <text class="company-name" x="449" y="290" font-size="64" text-anchor="middle">RVB Plumbing Services</text>
  </svg>

  <p class="side-label side-label--front">Front</p>

  <svg class="card card--back" viewBox="0 0 898 539" xmlns="http://www.w3.org/2000/svg">
    <rect class="card-edge" x="0.5" y="0.5" width="897" height="538"/>
    <polygon class="band-silver" points="0,304 252,539 0,539"/>
    <polygon class="band-sky" points="0,320 234,539 0,539"/>
    <polygon class="band-aqua" points="0,418 130,539 0,539"/>

    <text class="person-name" x="192" y="128" font-size="36" text-anchor="middle">Owen Tredgold</text>
    <text class="person-title" x="192" y="177" font-size="34" text-anchor="middle">Director</text>

    <text class="company-name" x="632" y="158" font-size="38" text-anchor="middle">RVB Plumbing Services</text>

    <text class="contact-line" x="751" y="350" font-size="32" text-anchor="end" letter-spacing="2">0431 862 507</text>
    <g class="icon-phone">
      <rect class="icon-fill" x="786" y="322" width="19" height="33" rx="3"/>
      <rect x="788.5" y="326" width="14" height="23" fill="var(--paper)"/>
      <circle cx="795.5" cy="351.5" r="1.4" fill="var(--paper)"/>
    </g>

    <text class="contact-line" x="751" y="402" font-size="30" text-anchor="end">owen@rvb-plumbing.com.au</text>
    <g class="icon-mail">
      <rect class="icon-fill" x="781" y="382" width="30" height="21"/>
      <polyline class="icon-stroke" points="781,382 796,395 811,382"/>
      <line class="icon-stroke" x1="781" y1="403" x2="792" y2="392"/>
      <line class="icon-stroke" x1="811" y1="403" x2="800" y2="392"/>
    </g>

    <polygon class="band-aqua" points="369,429 898,429 898,496 436,496"/>
    <text class="abn-line" x="751" y="476" font-size="34" text-anchor="end">ABN - 73 215 904 386</text>
  </svg>

  <p class="side-label side-label--back">Back</p>

</div>
</body>
</html>
```